Design a brochure for bulk SMS service provider

I need a brochure design for bulk SMS provder in South Sudan. The company provides API services for SMS, telephony airtime, bulk SMS and other value added SMS services. Our main product allow people and applications to send and receive SMS locally using our software gateway.
We already have the logo design and would like to see the same colors used in the brochure design. I have attached information data to use in the brochure. much of data is in form of lists. I would prefer a grid layout for list items with each having small icon that relates to information the list item communicates.
I have attached a some images of models to use in the design. such as cover page. you can add more images where you see fit.

Target Market(s)

East Africa Region

Industry/Entity Type

Technology, telecommunication, software

Requirements
Must have
• At least 4 brochure pages, all list items properly layout on grids with icons. I will provide icons for out clients section
Nice to have
• More extra images that convey the message well.
Should not have
• Direct copy of brief large text into one section. e.g Don't copy the use cases section verbatim in to page without design and formatting.

```html
<!DOCTYPE html>
<html lang="en">
<head>
<meta charset="utf-8">
<title>NilaText – Bulk SMS brochure</title>
<link href="https://fonts.googleapis.com/css2?family=Open+Sans:wght@300;400;600;700&display=swap" rel="stylesheet">
<style>
:root{
  --blue:#47bdea;
  --blue-light:#a6e0f6;
  --orange:#e8591f;
  --dark:#2b2526;
  --ink:#3c3c3c;
  --paper:#ffffff;
  --backdrop:#e8e5e0;
}
*{box-sizing:border-box;margin:0;padding:0}
html,body{width:1200px;height:900px;overflow:hidden;background:var(--backdrop);font-family:"Open Sans",sans-serif;color:var(--ink)}
.canvas{position:relative;width:1200px;height:900px}
.spread{position:absolute;width:690px;height:440px;background:var(--paper);box-shadow:0 3px 10px rgba(0,0,0,.18);overflow:hidden}
.spread--outer{left:30px;top:10px}
.spread--inner{left:480px;top:455px}
.page{position:absolute;top:0;width:345px;height:440px;overflow:hidden}
.page--left{left:0}
.page--right{left:345px}
.base-strip{position:absolute;left:0;right:0;bottom:0;height:7px;background:var(--blue)}
.url-tab{position:absolute;right:0;bottom:0;width:112px;height:24px;background:var(--dark);clip-path:polygon(10px 0,100% 0,100% 100%,0 100%);color:#fff;font-size:7.5px;display:flex;align-items:center;justify-content:center;padding-left:8px}
.brand{position:absolute;display:flex;align-items:center;gap:4px;font-weight:700;letter-spacing:-.2px}
.brand__dot{border-radius:50%;display:block}

/* back cover */
.back-wash{position:absolute;left:0;top:0}
.clients__title{position:absolute;left:58px;top:284px;color:var(--orange);font-size:8px;font-weight:600}
.clients__grid{position:absolute;left:58px;top:305px;display:grid;grid-template-columns:92px 82px 40px;row-gap:12px;align-items:center}
.client{font-size:10px;color:#1d9ad6;font-weight:400}
.client--seal{width:38px;height:38px;border-radius:50%;border:2px solid #9a9a9a;grid-row:1 / span 2;grid-column:3}
.contact{position:absolute;left:0;width:345px;top:390px;text-align:center;font-size:5.2px;line-height:1.6;color:#333}
.contact__title{font-size:8px;font-weight:600;margin-bottom:4px}
.contact b{font-weight:700}

/* front cover */
.cover-shape{position:absolute;left:0;top:0}
.cover-title{position:absolute;left:29px;top:374px;font-size:25px;font-weight:300;color:var(--orange)}

/* inner spread */
.about{position:absolute;left:0;top:0;width:345px;height:174px;background:var(--orange);color:#fff}
.about__title{position:absolute;left:28px;top:72px;font-size:11px;font-weight:600}
.about__text{position:absolute;left:28px;top:94px;width:282px;font-size:5.1px;line-height:1.5}
.about__text p+p{margin-top:6px}
.section-title{position:absolute;top:180px;color:var(--orange);font-size:10.5px;font-weight:600}
.section-rule{position:absolute;left:0;top:196px;width:345px;height:1px;background:#c8a27f}
.list{position:absolute;display:flex;flex-direction:column;list-style:none}
.list--features{left:28px;top:205px;width:172px;gap:6px}
.list--solutions{left:205px;top:205px;width:112px;gap:6px}
.item{display:flex;gap:9px;font-size:5.1px;line-height:1.45}
.item svg{flex:0 0 14px;width:14px;height:14px;margin-top:1px}
.item b{font-weight:700}
.phone-screen{position:absolute;left:228px;top:344px;width:58px;height:87px;border:1px solid #7b8590;border-radius:3px;background:#c9d3ee}
.phone-screen__bar{position:absolute;left:0;right:0;top:0;height:4px;background:#e6e9ef}
.phone-screen__base{position:absolute;left:0;right:0;bottom:0;height:5px;background:#e6e9ef}
.bubble{position:absolute;border-radius:2px;border:1px solid #555}
.bubble--out1{left:22px;top:12px;width:32px;height:12px;background:#2f9a3c;color:#fff;font-size:2.6px;padding:2px}
.bubble--in{left:4px;top:32px;width:24px;height:16px;background:#eceff3}
.bubble--out2{left:22px;top:56px;width:32px;height:16px;background:#2f9a3c}
.hands-photo{position:absolute;left:0;top:0;width:345px;height:196px}
.usecase-band{position:absolute;left:0;top:196px;width:345px;height:31px;background:var(--dark);border-top:1px solid #b4582b;color:#fff;font-size:10.5px;font-weight:600;display:flex;align-items:center;justify-content:center}
.usecases{position:absolute;left:36px;top:237px;width:290px;columns:2;column-gap:24px;font-size:5.1px;line-height:1.45}
.usecases p{margin-bottom:5px}
.usecases b{font-weight:700}
</style>
</head>
<body>
<div class="canvas">

  <!-- outer spread: back cover + front cover -->
  <section class="spread spread--outer">
    <div class="page page--left">
      <svg class="back-wash" width="345" height="320" viewBox="0 0 345 320" aria-hidden="true">
        <path d="M0 0H345V175Q262 312 95 303Q40 300 0 282Z" fill="var(--blue-light)"/>
      </svg>
      <h3 class="clients__title">Our clients</h3>
      <div class="clients__grid">
        <span class="client">Brightwell Aid</span>
        <span class="client">ShopMarket</span>
        <span class="client client--seal"></span>
        <span class="client">FieldPoll</span>
        <span class="client">Carewell Health</span>
      </div>
      <div class="contact">
        <div class="contact__title">Contact us</div>
        <div><b>Address</b>: Kator Plaza office No. 7, Central Equatoria State, Juba – South Sudan</div>
        <div><b>Emails</b>: Sales: sales@nilatext.com &nbsp;|&nbsp; Support: info@nilatext.com</div>
        <div><b>Telephone</b>: +211 920 555 014</div>
      </div>
    </div>
    <div class="page page--right">
      <svg class="cover-shape" width="345" height="440" viewBox="0 0 345 440">
        <circle cx="210" cy="211" r="179" fill="var(--blue)"/>
        <defs>
          <radialGradient id="coverPhoto" cx="45%" cy="40%" r="65%">
            <stop offset="0" stop-color="#eef0f2"/>
            <stop offset=".55" stop-color="#d6d9dc"/>
            <stop offset="1" stop-color="#b9bcc0"/>
          </radialGradient>
        </defs>
        <circle cx="221" cy="176" r="146" fill="url(#coverPhoto)" role="img" aria-label="Photo: smiling young woman texting on her phone, with envelope icons rising from it"/>
      </svg>
      <div class="brand" style="left:20px;top:22px;font-size:22px;color:var(--dark)">
        <span class="brand__dot" style="width:20px;height:20px;background:var(--dark)"></span>NilaText
      </div>
      <h1 class="cover-title">Bulk SMS service</h1>
      <div class="url-tab">www.nilatext.com</div>
    </div>
    <div class="base-strip"></div>
  </section>

  <!-- inner spread -->
  <section class="spread spread--inner">
    <div class="page page--left">
      <div class="about">
        <div class="brand" style="left:18px;top:14px;font-size:16px;color:#fff">
          <span class="brand__dot" style="width:16px;height:16px;background:#fff"></span>NilaText
        </div>
        <h2 class="about__title">About us</h2>
        <div class="about__text">
          <p><b>NilaText</b> is a bulk SMS provider in South Sudan having 5+ years experience in providing multi-routes message solutions to promote your business. Increase sales and customer satisfaction with smarter SMS campaigns, instant OTPs, notifications, two-way interactions, and other innovative bulk SMS services.</p>
          <p>Our focus is to facilitate SMS routing and delivery and as well as help businesses hop through myriad of regulations put forth by authorities in South Sudan. Using our many partner telecommunication providers, we are able to push your message on a predictable route and be sure of delivery.</p>
        </div>
      </div>
      <h3 class="section-title" style="left:27px">Our features</h3>
      <h3 class="section-title" style="left:205px">Our Solutions</h3>
      <div class="section-rule"></div>

      <ul class="list list--features">
        <li class="item"><svg viewBox="0 0 14 14" fill="none" stroke="var(--blue)"><path d="M2 7L12 2 9 12 7 8Z"/></svg><span><b>Send SMS</b> - Easily Send SMS with different methods (web, http, smpp)</span></li>
        <li class="item"><svg viewBox="0 0 14 14" fill="none" stroke="var(--blue)"><path d="M12 7L2 12 5 2 7 6Z"/></svg><span><b>Receive SMS</b> - Easily receive SMS in South Sudan using a combination of catchy keywords, short codes and long codes provided by NilaText</span></li>
        <li class="item"><svg viewBox="0 0 14 14" fill="var(--blue)"><circle cx="7" cy="4" r="2.2"/><circle cx="3.5" cy="10" r="2.2"/><circle cx="10.5" cy="10" r="2.2"/></svg><span><b>Auto Responders</b> – Easily compose an automated SMS response that is sent to every customer who texts to your short code</span></li>
        <li class="item"><svg viewBox="0 0 14 14" fill="none" stroke="var(--blue)"><path d="M2 5H12M9 2L12 5 9 8M12 9H2M5 6L2 9 5 12"/></svg><span><b>Two Way SMS</b> – You can request short codes, long codes or even use one of our shared short codes to receive and send messages to your customer. Create unlimited keywords on these codes too.</span></li>
        <li class="item"><svg viewBox="0 0 14 14" fill="none" stroke="var(--blue)"><circle cx="7" cy="7" r="5.5"/><path d="M4.5 6H9.5M4.5 8.5H9.5"/></svg><span><b>SMS Polls</b> - Conduct polls, interact with customers, and build your database by receiving SMS</span></li>
        <li class="item"><svg viewBox="0 0 14 14" fill="none" stroke="var(--blue)"><path d="M1 8L13 2 9 12 7 9Z"/></svg><span><b>Airtime</b> – Send airtime easily to your customers in South Sudan using our simple REST API feature.</span></li>
        <li class="item"><svg viewBox="0 0 14 14" fill="none" stroke="var(--blue)"><rect x="2" y="1.5" width="10" height="11"/><path d="M5 10V8M7 10V6M9 10V4"/></svg><span><b>Delivery Reports</b> - Know at any given time the status of outgoing SMS sent using any of our various methods.</span></li>
        <li class="item"><svg viewBox="0 0 14 14" fill="none" stroke="var(--blue)"><rect x="1.5" y="1.5" width="6" height="8"/><rect x="6.5" y="4.5" width="6" height="8"/></svg><span><b>USSD</b> – easily build interactive aplications on top of USSD framework</span></li>
      </ul>

      <ul class="list list--solutions">
        <li class="item"><svg viewBox="0 0 14 14" fill="none" stroke="var(--blue)"><circle cx="7" cy="7" r="5.5"/><path d="M4 7H10M7 4V10"/></svg><span><b>SMS aggregation</b> – Send and receive SMS easily from any network in South Sudan</span></li>
        <li class="item"><svg viewBox="0 0 14 14" fill="none" stroke="var(--blue)"><path d="M1 7L13 2 9 12Z"/><path d="M4 10L2 13"/></svg><span><b>Bulk SMS</b> – Send to multiple people at the same time using one request.</span></li>
        <li class="item"><svg viewBox="0 0 14 14" fill="none" stroke="var(--blue)"><rect x="4" y="1.5" width="6" height="11" rx="1"/><path d="M6 10.5H8"/></svg><span><b>Airtime</b> - Provide airtime distribution services to mobile phone users in South Sudan</span></li>
        <li class="item"><svg viewBox="0 0 14 14" fill="none" stroke="var(--blue)"><circle cx="7" cy="7" r="2.5"/><circle cx="7" cy="7" r="5.5" stroke-dasharray="2 1.5"/></svg><span><b>USSD</b> – Build interactive applications using our USSD API</span></li>
        <li class="item"><svg viewBox="0 0 14 14" fill="none" stroke="var(--blue)"><rect x="3" y="1" width="8" height="12" rx="1"/><path d="M5 4H9M5 6.5H9M5 9H9"/></svg><span><b>Short codes</b> – Offer short numbers to send and receive SMS in South Sudan.</span></li>
      </ul>

      <div class="phone-screen">
        <div class="phone-screen__bar"></div>
        <div class="bubble bubble--out1">Put your own text in the message boxes</div>
        <div class="bubble bubble--in"></div>
        <div class="bubble bubble--out2"></div>
        <div class="phone-screen__base"></div>
      </div>
    </div>

    <div class="page page--right">
      <svg class="hands-photo" viewBox="0 0 345 196" preserveAspectRatio="none" role="img" aria-label="Photo: hands tapping a smartphone with glowing envelope icons and warm bokeh lights above it">
        <defs>
          <radialGradient id="handsPhoto" cx="65%" cy="35%" r="75%">
            <stop offset="0" stop-color="#d58a3e"/>
            <stop offset=".35" stop-color="#8a4a2a"/>
            <stop offset=".7" stop-color="#4a3230"/>
            <stop offset="1" stop-color="#2b2526"/>
          </radialGradient>
        </defs>
        <rect width="345" height="196" fill="url(#handsPhoto)"/>
      </svg>
      <div class="usecase-band">Use cases</div>
      <div class="usecases">
        <p><b>Marketing and Ads</b> – Easily send promotional messages using our platform. Whether it is personalizing millions of texts via multiple merge fields, sending regional language texts, sharing images and files via SMS, staggering large pushes in batches, it is all incredibly easy with NilaText</p>
        <p><b>Banking and Financial services</b> - 1) Send transnational alerts 2) Send SMS campaign your customers love. Our platform provide powerful personalization features 3) Control queue using SMS supported applications.</p>
        <p><b>NGO</b> – 1) No need to hand out pamphlets or send them via post. Easily create and send memorable promotional SMS campaigns 2) Keep your donors regularly updated with reports and news of activities through a simple SMS that includes web links to relevant information 3) Remote areas communication using SMS. Build apps on top of our gateway that can support your on site team.</p>
        <p><b>Healthcare</b> - 1) Send automated confirmations and reminders for doctor appointments, medical tests 2) Issue mobile visitor passes to patients' visitors and limit access to the patient rooms using SMS 3) Allow patients to seek appointments by texting the time slot to the hospital's SMS inbox setup using short code or long code services 4) Allow patients to request emergency assistance by texting in a pre-defined keyword to your SMS inbox.</p>
        <p><b>Restaurant and takeways</b> – 1) encourage restaurant visitors to text into your SMS longcodes/shortcodes to receive special invites and offers. Grow your opt-in database. 2) Entice customers with limited time discount vouchers for lean hours sent via SMS.</p>
        <p><b>Education</b> – 1) Use bulk SMS to send information about exam schedules, reading material, and meeting invites to students, parents and staff. 2) allow student to query exams results using two way SMS 3) Get real time and quick feedback about students, teachers, courses and facilities using SMS surveys.</p>
      </div>
      <div class="url-tab">www.nilatext.com</div>
    </div>
    <div class="base-strip" style="right:112px"></div>
  </section>

</div>
</body>
</html>
```